Calloway Brewhouse Beer Can Design

Design a beer can for a boutique craft brewery located in Frankston, Victoria, AUS.
We have a focus on producing socially approachable beers in an ambient setting. The beer can design should be sophisticated, simple, recognizable and a little playful. The color pallet should be inviting and not too bold. The design should have identifying features that can be interchanged onto different cans for different beer types. The design must be repeatable for other beer varieties, which will each have a unique color. The can should feature black, white and purple (this should be in interchangeable color). The beer can also needs to have our Calloway Brewhouse company logo on it, this has been attached to the design brief.

Target Market(s)

The target market is aged 25+ who are social, have some disposable income and appreciate good beer, wine and food.
The beers will also be made for distribution, initially to locally to restaurants and cafés and eventually commercially.
Tourists will also be targeted due to the area the brewhouse is located (Mornington Peninsula, Victoria, AUS).

Industry/Entity Type

Hospitality

Font styles to use
Sans Serif
Script

Colors
6b449b
876aae
b7a5cd
e4daeb
000000
ffffff
959595

Requirements
Must have
• The ‘Calloway Brewhouse’ logo.
• The colour associated to this beer - purple. This should be the only colour used on the can (along with black/white/gray).
• The company tagline ‘Socially Approachable’.
• The tasting notes text ‘Bright in colour, dry on the palate and thirst quenching in the extreme, wheat and pale malts compliment each other with nuance.’
• Australian beer can requirements as per 'Requirements.png'. EPS and AI files of the requirements have been included.
Nice to have
• The logo text ‘Wendel Malt IPA’ more predominant than the Calloway Brewhouse logo.
Should not have
• Be busy, simple is best
• Beer related pictures / images
• Bold, masculine lines and fonts
• Requirements.png directly used. Please use the EPS or AI files provided.

```html
<!DOCTYPE html>
<html lang="en">
<head>
<meta charset="utf-8">
<title>Calloway Brewhouse – Wendel Malt IPA Can Label</title>
<link rel="stylesheet" href="https://fonts.googleapis.com/css2?family=Federo&family=Playfair+Display:wght@700&family=Caveat:wght@500&family=Roboto+Condensed:wght@300;400&display=swap">
<style>
  :root {
    --backdrop: #121212;
    --purple: #6b449b;
    --purple-deep: #4e2c7d;
    --purple-light: #876aae;
    --lavender: #b7a5cd;
    --mist: #e4daeb;
    --black: #000000;
    --ink: #1c1c1c;
    --white: #ffffff;
    --grey: #959595;
    --silver: #c9c9c9;
    --silver-light: #dcdcdc;
  }
  * { box-sizing: border-box; margin: 0; padding: 0; }
  html, body { width: 814px; height: 1200px; overflow: hidden; background: var(--backdrop); }
  .canvas { position: relative; width: 814px; height: 1200px; }

  .label {
    position: absolute; left: 92px; top: 70px; width: 630px; height: 1060px;
    border-radius: 6px; overflow: hidden;
  }
  .label__upper {
    position: absolute; left: 0; top: 0; width: 100%; height: 420px;
    background: linear-gradient(90deg, var(--grey) 0%, var(--silver-light) 30%, var(--silver) 70%, var(--grey) 100%);
  }
  .tab { position: absolute; left: 50%; top: 0; width: 190px; height: 115px; transform: translateX(-50%); }

  .brand {
    position: absolute; left: 0; right: 0; top: 190px; text-align: center;
    font-family: "Roboto Condensed", sans-serif; font-weight: 300;
    color: var(--ink); text-transform: uppercase;
  }
  .brand__name { font-size: 66px; letter-spacing: 4px; line-height: 1; display: block; }
  .brand__sub { font-size: 42px; letter-spacing: 14px; line-height: 1.3; display: block; }

  .divider { position: absolute; left: 0; width: 100%; top: 420px; height: 14px; background: var(--ink); border-bottom: 4px solid var(--grey); }

  .label__lower {
    position: absolute; left: 0; top: 434px; width: 100%; height: 626px;
    background: linear-gradient(90deg, var(--purple-deep) 0%, var(--purple) 30%, var(--purple) 70%, var(--purple-deep) 100%);
    text-align: center; color: var(--white);
  }
  .beer-name { white-space: nowrap; }
  .beer-name__first {
    display: block; margin-top: 40px;
    font-family: "Playfair Display", serif; font-weight: 700; font-size: 66px; line-height: 1; letter-spacing: 1px;
    color: var(--white);
  }
  .beer-name__second {
    display: block; margin-top: 12px;
    font-family: "Federo", sans-serif; font-size: 118px; line-height: 1; letter-spacing: -1px;
    color: var(--silver-light);
  }
  .rule { width: 490px; margin: 24px auto 0; border-top: 2px dotted var(--lavender); opacity: .7; }
  .tagline {
    font-family: "Caveat", cursive; font-weight: 500; font-size: 54px; line-height: 1.2;
    color: var(--mist); margin-top: 10px; white-space: nowrap;
  }
  .tagline + .rule { margin-top: 12px; }
  .notes {
    width: 450px; margin: 22px auto 0;
    font-family: "Roboto Condensed", sans-serif; font-weight: 300; font-size: 14px; line-height: 1.55;
    color: var(--mist);
  }
  .specs {
    position: absolute; left: 50%; bottom: 0; transform: translateX(-50%);
    display: flex; align-items: center; gap: 10px;
    background: var(--ink); border-radius: 12px 12px 0 0; padding: 14px 18px 20px;
    font-family: "Roboto Condensed", sans-serif; color: var(--white);
  }
  .specs__stats { font-size: 14px; line-height: 1.2; text-align: right; padding-right: 10px; border-right: 2px dotted var(--grey); }
  .specs__volume { font-size: 38px; font-weight: 400; line-height: 1; }
</style>
</head>
<body>
<main class="canvas">
  <section class="label">
    <div class="label__upper">
      <svg class="tab" viewBox="0 0 190 115" aria-hidden="true">
        <polygon points="0,0 190,0 95,115" fill="#1c1c1c"/>
        <circle cx="95" cy="46" r="22" fill="#6b449b"/>
      </svg>
      <div class="brand">
        <span class="brand__name">Calloway</span>
        <span class="brand__sub">Brewhouse</span>
      </div>
    </div>
    <div class="divider"></div>
    <div class="label__lower">
      <h1 class="beer-name">
        <span class="beer-name__first">WENDEL</span>
        <span class="beer-name__second">MALT IPA</span>
      </h1>
      <div class="rule"></div>
      <p class="tagline">Socially Approachable</p>
      <div class="rule"></div>
      <p class="notes">Bright in colour, dry on the palate and thirst quenching in the extreme, wheat and pale malts compliment each other with nuance.</p>
      <div class="specs">
        <div class="specs__stats">ABV 4.8%<br>IBU 22</div>
        <div class="specs__volume">330ML</div>
      </div>
    </div>
  </section>
</main>
</body>
</html>
```